Creative Graphic Designer needed to create fabulous wash cloths

We are an Interior design business and are releasing a range of wash cloths.
We would like some innovative designs to have screen printed on these cloths.
We will only be printing on one side.

The size of the cloth is 18 cm x 20 cm and the colour of the cloth is variable.

At this stage we have selected white, turquoise, orange and apple green as the base colours we require. (see attached)

1. The first design should portray 'used for washing up' and
2. the second 'used for wiping around'. Or just 'wiping only' sink only.

These can be in image format or a combination of image and text.

I am happy for you to use the whole of the cloth, or as little as you see fit.

I would see two print colours or max three, onto the base cloth.

I have also attached our company logo which I would like incorporated somewhere on the cloth, it can be as small or large as you like.
We are looking for something really creative.

Thanks so much!

Target Market(s)

Medium to high end

Industry/Entity Type

Graphic Designer

Requirements
Must have
• include the logo somewhere on the wash cloth. Final design must be in .eps or pdf. and PANTONE colours.
Nice to have
• Something really fun and creative, however we are looking for originality
• I have included some concepts previously done to show what can be done.
• I dont mind if they are images, scenes, text, whatever you feel portrays the 'use for in the sink' and use for wiping around best.
• The attached image of New York I particularly like, I understand it has used alot more colours, but I found the concept really nice.
Should not have
• More than three colours.

```html
<!DOCTYPE html>
<html lang="en">
<head>
<meta charset="utf-8">
<title>Wash Cloth Designs – Wash Up &amp; Wipe Up</title>
<link href="https://fonts.googleapis.com/css2?family=Mrs+Saint+Delafield&family=Montserrat:wght@600&display=swap" rel="stylesheet">
<style>
  :root {
    --board: #000000;
    --cream: #eeeee6;
    --turquoise: #2bb3a3;
    --turquoise-deep: #1a9a92;
    --apple: #9cc95a;
    --orange: #e8874a;
    --ink-teal: #1d4f50;
    --print-white: #ffffff;
    --mark-dark: #1b2a2a;
  }
  * { margin: 0; padding: 0; box-sizing: border-box; }
  html, body {
    width: 1200px;
    height: 785px;
    overflow: hidden;
    background: var(--board);
  }
  .sheet {
    position: relative;
    width: 1200px;
    height: 785px;
    background: var(--board);
  }
  .cloth {
    position: absolute;
    width: 347px;
    height: 386px;
    overflow: hidden;
  }
  .col-1 { left: 0; }
  .col-2 { left: 364px; }
  .col-3 { left: 853px; }
  .row-1 { top: 0; }
  .row-2 { top: 399px; }

  .floral-print {
    position: absolute;
    inset: 0;
    background:
      radial-gradient(ellipse 48% 40% at 50% 52%, var(--turquoise) 0%, var(--turquoise-deep) 45%, rgba(43,179,163,0) 75%),
      radial-gradient(circle at 12% 8%, rgba(43,179,163,0.55) 0%, rgba(43,179,163,0) 30%),
      radial-gradient(circle at 92% 90%, rgba(156,201,90,0.5) 0%, rgba(156,201,90,0) 30%),
      radial-gradient(circle at 30% 22%, rgba(232,135,74,0.35) 0%, rgba(232,135,74,0) 22%),
      radial-gradient(circle at 80% 60%, rgba(232,135,74,0.25) 0%, rgba(232,135,74,0) 20%),
      var(--cream);
  }
  .cloth-word {
    position: absolute;
    left: 0;
    right: 0;
    top: 142px;
    text-align: center;
    font-family: "Mrs Saint Delafield", cursive;
    font-size: 66px;
    line-height: 1;
    letter-spacing: 4px;
  }
  .word-dark { color: var(--ink-teal); }
  .word-light { color: var(--print-white); }
  .word-wide { letter-spacing: 8px; font-size: 60px; }

  .brand {
    position: absolute;
    left: 0;
    right: 0;
    bottom: 22px;
    display: flex;
    justify-content: center;
    align-items: center;
    gap: 6px;
  }
  .brand-square {
    width: 10px;
    height: 10px;
    background: var(--mark-dark);
  }
  .brand-name {
    font-family: "Montserrat", sans-serif;
    font-weight: 600;
    font-size: 13px;
    letter-spacing: 1px;
    color: var(--mark-dark);
  }
</style>
</head>
<body>
<main class="sheet">

  <section class="cloth col-1 row-1">
    <div class="floral-print" role="img" aria-label="Watercolour turquoise wash with outlined orange, apple-green and teal flowers and leaves"></div>
    <p class="cloth-word word-dark">wash up</p>
    <div class="brand"><span class="brand-square"></span><span class="brand-name">Fernhouse</span></div>
  </section>

  <section class="cloth col-2 row-1">
    <div class="floral-print" role="img" aria-label="Watercolour turquoise wash with outlined orange, apple-green and teal flowers and leaves"></div>
    <p class="cloth-word word-light">wash up</p>
    <div class="brand"><span class="brand-square"></span><span class="brand-name">Fernhouse</span></div>
  </section>

  <section class="cloth col-3 row-1">
    <div class="floral-print" role="img" aria-label="Watercolour turquoise wash with outlined orange, apple-green and teal flowers and leaves"></div>
    <p class="cloth-word word-light word-wide">wash up</p>
    <div class="brand"><span class="brand-square"></span><span class="brand-name">Fernhouse</span></div>
  </section>

  <section class="cloth col-1 row-2">
    <div class="floral-print" role="img" aria-label="Watercolour turquoise wash with outlined orange, apple-green and teal flowers and leaves"></div>
    <p class="cloth-word word-dark">wipe up</p>
    <div class="brand"><span class="brand-square"></span><span class="brand-name">Fernhouse</span></div>
  </section>

  <section class="cloth col-2 row-2">
    <div class="floral-print" role="img" aria-label="Watercolour turquoise wash with outlined orange, apple-green and teal flowers and leaves"></div>
    <p class="cloth-word word-light">wipe up</p>
    <div class="brand"><span class="brand-square"></span><span class="brand-name">Fernhouse</span></div>
  </section>

  <section class="cloth col-3 row-2">
    <div class="floral-print" role="img" aria-label="Watercolour turquoise wash with outlined orange, apple-green and teal flowers and leaves"></div>
    <p class="cloth-word word-light word-wide">wipe up</p>
    <div class="brand"><span class="brand-square"></span><span class="brand-name">Fernhouse</span></div>
  </section>

</main>
</body>
</html>
```